Floor Inspections and Consulting

We provide inspections and consulting services on various floor coverings, e.g. carpet, hardwood, etc. We also do expert witness work for attorneys due to floor covering failures. We current have a logo, just need it incorporated into a new design. I have examples of cards I have found on the internet that capture my attention and make a statement. I have included our original business card, which in my opinion is terrible, but it does have our logo on it.

```html
<!DOCTYPE html>
<html lang="en">
<head>
<meta charset="utf-8">
<title>Keystone Floor Inspections – Business Card</title>
<link rel="stylesheet" href="https://fonts.googleapis.com/css2?family=Montserrat:wght@700&family=Rubik:wght@400;500&display=swap">
<style>
  :root {
    --backdrop: #e6e6e6;
    --yellow: #fbc314;
    --ink: #232323;
    --night: #0b0c10;
    --night-soft: #1d1f24;
    --paper: #ffffff;
    --muted: #6f6f6f;
  }
  html, body {
    margin: 0;
    width: 1200px;
    height: 1200px;
    overflow: hidden;
    background: var(--backdrop);
  }
  .card {
    position: absolute;
    left: 188px;
    width: 824px;
    height: 470px;
    overflow: hidden;
  }
  .card-front {
    top: 93px;
    background: radial-gradient(ellipse at 60% 45%, var(--night-soft) 0%, var(--night) 75%);
  }
  .card-back {
    top: 636px;
    background: var(--paper);
  }
  .swoosh {
    position: absolute;
    left: 0;
    top: 0;
    width: 824px;
    height: 470px;
  }
  .brand {
    position: absolute;
    display: flex;
    flex-direction: column;
    align-items: center;
    text-align: center;
    font-family: "Rubik", sans-serif;
  }
  .brand-dot {
    width: 34px;
    height: 34px;
    border-radius: 50%;
    margin-bottom: 16px;
  }
  .brand-name {
    font-weight: 500;
    font-size: 30px;
    line-height: 1.15;
    letter-spacing: 1px;
  }
  .tagline {
    position: absolute;
    font-family: "Rubik", sans-serif;
    font-weight: 500;
    letter-spacing: 0.5px;
    white-space: nowrap;
    transform: translateX(-50%);
  }
  .card-front .brand {
    left: 542px;
    top: 220px;
    transform: translate(-50%, -50%);
    color: var(--paper);
  }
  .card-front .brand-dot { background: var(--paper); }
  .card-front .tagline {
    left: 545px;
    top: 340px;
    font-size: 17px;
    color: var(--paper);
  }
  .card-back .brand {
    left: 660px;
    top: 200px;
    transform: translate(-50%, -50%);
    color: var(--ink);
  }
  .card-back .brand-name { font-size: 26px; }
  .card-back .brand-dot { background: var(--ink); width: 30px; height: 30px; }
  .card-back .tagline {
    left: 660px;
    top: 304px;
    font-size: 14px;
    color: var(--ink);
  }
  .person-name {
    position: absolute;
    left: 154px;
    top: 140px;
    margin: 0;
    font-family: "Montserrat", sans-serif;
    font-weight: 700;
    font-size: 31px;
    letter-spacing: 1px;
    color: var(--ink);
  }
  .contact {
    position: absolute;
    left: 154px;
    top: 222px;
    margin: 0;
    padding: 0;
    list-style: none;
    font-family: "Rubik", sans-serif;
    font-size: 18px;
    color: var(--muted);
    letter-spacing: 0.4px;
  }
  .contact li { line-height: 26px; }
  .contact .website { margin-top: 13px; }
</style>
</head>
<body>

<section class="card card-front" aria-label="Card front">
  <svg class="swoosh" viewBox="0 0 824 470" aria-hidden="true">
    <path d="M0 0 H192 C205 110 300 200 288 320 C280 400 225 445 165 470 H0 Z" fill="var(--yellow)"/>
  </svg>
  <div class="brand">
    <span class="brand-dot"></span>
    <span class="brand-name">KEYSTONE<br>FLOOR INSPECTIONS</span>
  </div>
  <div class="tagline">ANALYSIS &amp; CONSULTING</div>
</section>

<section class="card card-back" aria-label="Card back">
  <svg class="swoosh" viewBox="0 0 824 470" aria-hidden="true">
    <path d="M0 0 H54 C68 110 142 180 137 290 C133 380 85 440 22 470 H0 Z" fill="var(--yellow)"/>
  </svg>
  <h1 class="person-name">DANIEL MORROW</h1>
  <ul class="contact">
    <li>303-555-0142</li>
    <li>dan@keystonefloorcheck.com</li>
    <li class="website">KEYSTONEFLOORCHECK.COM</li>
  </ul>
  <div class="brand">
    <span class="brand-dot"></span>
    <span class="brand-name">KEYSTONE<br>FLOOR INSPECTIONS</span>
  </div>
  <div class="tagline">ANALYSIS &amp; CONSULTING</div>
</section>

</body>
</html>
```